Business Card Design for Small Electrical Contractor

I need to update my business card into something a little more modern. We are a small electrical contracting company. We service domestic and commercial places around Sydney. We have 2 logo designs at the moment. I have uploaded both and 2 different sizes to work with.

Industry/Entity Type

Business

Contact Information for Business Card

Ted Corbin
8/21-23 Holt St, Fernhaven 2087
t - (02) 9471 3820
m - 0427 915 304
E - info@corbinelec.example.au
W - corbinelec.example.au
ABN: 42 907 518 263

Font styles to use
Sans Serif

Requirements
Must have
• I would also like to see the below fit on somewhere aswell
• - Licensed Electrician
• - Level 2 (Cat 1 & 4)
• - Domestic
• - Commercial
• - Repairs and Installations
• - Data
Nice to have
• Try and keep similar colours as logo
Should not have
• No lightning bolts or light globes. Smart and professional please.

```html
<!DOCTYPE html>
<html lang="en">
<head>
<meta charset="utf-8">
<title>Corbin Electrical – Business Card</title>
<link href="https://fonts.googleapis.com/css2?family=Lato:wght@400;700&display=swap" rel="stylesheet">
<style>
  :root {
    --bg: #e9e7e3;
    --green: #123a37;
    --orange: #f39a1e;
    --white: #ffffff;
    --ink: #1d1d1d;
    --light: #f1f1ee;
  }
  * { box-sizing: border-box; margin: 0; padding: 0; }
  html, body { width: 1200px; height: 900px; overflow: hidden; }
  body {
    background: var(--bg);
    font-family: 'Lato', Arial, sans-serif;
    display: flex;
    align-items: center;
    justify-content: center;
    gap: 40px;
  }
  .card {
    width: 540px;
    height: 330px;
    position: relative;
    overflow: hidden;
    box-shadow: 0 6px 18px rgba(0,0,0,0.18);
  }
  .card--front { background: var(--green); color: var(--light); }
  .brand {
    position: absolute;
    display: flex;
    flex-direction: column;
    align-items: flex-start;
  }
  .brand__name {
    font-weight: 700;
    color: var(--light);
    letter-spacing: 1px;
    white-space: nowrap;
  }
  .brand__rule {
    height: 2px;
    background: var(--orange);
    margin-top: 6px;
  }
  .card--front .brand { top: 46px; left: 70px; }
  .card--front .brand__name { font-size: 38px; }
  .card--front .brand__rule { width: 400px; }
  .services {
    position: absolute;
    left: 250px;
    top: 180px;
    list-style: none;
    font-size: 15px;
    line-height: 1.35;
    color: var(--light);
  }
  .services li::before {
    content: "";
    display: inline-block;
    width: 5px; height: 5px;
    border-radius: 50%;
    background: var(--orange);
    margin-right: 8px;
    vertical-align: middle;
  }
  .card--back { background: var(--white); display: flex; }
  .back__panel {
    width: 210px;
    background: var(--green);
    border-right: 3px solid var(--orange);
    position: relative;
  }
  .card--back .brand { top: 70px; left: 22px; }
  .card--back .brand__name { font-size: 22px; }
  .card--back .brand__rule { width: 170px; }
  .contact {
    padding: 44px 0 0 36px;
    color: var(--ink);
  }
  .contact__name { font-size: 26px; font-weight: 400; }
  .contact__role { font-size: 16px; color: var(--orange); margin-top: 2px; }
  .contact__address { font-size: 16px; line-height: 1.3; margin-top: 10px; }
  .contact__list { list-style: none; margin-top: 8px; font-size: 16px; line-height: 1.45; }
  .contact__list li { display: flex; align-items: center; gap: 10px; }
  .contact__list svg { width: 14px; height: 14px; flex: none; fill: var(--orange); }
</style>
</head>
<body>
  <section class="card card--front">
    <div class="brand">
      <span class="brand__name">Corbin Electrical</span>
      <span class="brand__rule"></span>
    </div>
    <ul class="services">
      <li>Licensed Electrician</li>
      <li>Level 2 (Cat 1 &amp; 4)</li>
      <li>Domestic</li>
      <li>Commercial</li>
      <li>Repairs and Installations</li>
      <li>Data</li>
    </ul>
  </section>

  <section class="card card--back">
    <div class="back__panel">
      <div class="brand">
        <span class="brand__name">Corbin Electrical</span>
        <span class="brand__rule"></span>
      </div>
    </div>
    <div class="contact">
      <h1 class="contact__name">Ted Corbin</h1>
      <p class="contact__role">Owner</p>
      <p class="contact__address">8/21-23 Holt St<br>Fernhaven 2087</p>
      <ul class="contact__list">
        <li><svg viewBox="0 0 24 24" aria-hidden="true"><path d="M6.6 10.8a15.1 15.1 0 006.6 6.6l2.2-2.2a1 1 0 011-.25 11.4 11.4 0 003.6.6 1 1 0 011 1V20a1 1 0 01-1 1A17 17 0 013 4a1 1 0 011-1h3.5a1 1 0 011 1c0 1.25.2 2.45.6 3.6a1 1 0 01-.25 1z"/></svg>(02) 9471 3820</li>
        <li><svg viewBox="0 0 24 24" aria-hidden="true"><path d="M7 1h10a2 2 0 012 2v18a2 2 0 01-2 2H7a2 2 0 01-2-2V3a2 2 0 012-2zm0 3v14h10V4zm5 15.2a1.2 1.2 0 100 2.4 1.2 1.2 0 000-2.4z"/></svg>0427 915 304</li>
        <li><svg viewBox="0 0 24 24" aria-hidden="true"><path d="M2 5h20v14H2zm2 2v.5l8 5 8-5V7zm0 2.8V17h16V9.8l-8 5z"/></svg>info@corbinelec.example.au</li>
        <li><svg viewBox="0 0 24 24" aria-hidden="true"><path d="M12 2a10 10 0 100 20 10 10 0 000-20zm6.9 6h-2.9a15.6 15.6 0 00-1.4-3.6A8 8 0 0118.9 8zM12 4c.8 1.2 1.5 2.5 1.9 4h-3.8c.4-1.5 1.1-2.8 1.9-4zM4.3 14a8 8 0 010-4h3.4a16 16 0 000 4zm.8 2h2.9a15.6 15.6 0 001.4 3.6A8 8 0 015.1 16zM8 8H5.1a8 8 0 014.3-3.6A15.6 15.6 0 008 8zm4 12c-.8-1.2-1.5-2.5-1.9-4h3.8c-.4 1.5-1.1 2.8-1.9 4zm2.3-6H9.7a14.5 14.5 0 010-4h4.6a14.5 14.5 0 010 4zm.3 5.6A15.6 15.6 0 0016 16h2.9a8 8 0 01-4.3 3.6zM16.3 14a16 16 0 000-4h3.4a8 8 0 010 4z"/></svg>corbinelec.example.au</li>
      </ul>
    </div>
  </section>
</body>
</html>
```